Admin Backend Redesign

We need a redesign for our backend which supoosed to make the backoffice look more modern!

I will add screenshots of the backoffice so you know what data will be shown in the Admin.

Have in mind that the users of this backend are Doctors. We need a clinical look, modern and sharp. The backoffice is responsive, have that in mind. We need the backoffice to look as professional as possible.

The theme used for the website is: http://velmora.brisk-sample.net/

ON the main page of the backoffice, under every widget i need some space to write an explanation what the widget is about.

The color code used in our logo and website is #57aad4 combined with white.

We are open for ideas!
Updates

Project Deadline Extended
Reason: Designs are ok, but nothing innovative. Please use more modern designs!

Project Deadline Extended
Reason: Havent recieved a perfect design yet. Please read instructions carefully! Thank you

Project Deadline Extended
Reason: Hey everybody, sorry for the delay. We will decide in 3 days. If anyone wants to add a Design, that would be great.

Target Market(s)

Doctors, therapists

Industry/Entity Type

It Professional

Font styles to use
Sans Serif

Requirements
Must have
• Must look uptodate, modern, like new back offices look nowadays

```html
<!DOCTYPE html>
<html lang="de">
<head>
<meta charset="utf-8">
<title>Dashboard – Backoffice</title>
<link rel="stylesheet" href="https://fonts.googleapis.com/css2?family=Open+Sans:wght@300;400;600&display=swap">
<style>
:root{
  --brand:#57aad4;
  --crimson:#bf0000;
  --orange:#f95f2d;
  --coral:#f0603f;
  --lime:#75d13f;
  --ok:#3cc43a;
  --side:#303030;
  --side-line:#262626;
  --page:#f1f1f1;
  --line:#e2e2e2;
  --text:#333;
  --muted:#666;
  --white:#fff;
}
*{box-sizing:border-box;margin:0;padding:0}
html,body{width:1127px;height:1200px;overflow:hidden}
body{font-family:"Open Sans",sans-serif;background:var(--page);color:var(--text);position:relative}
.topbar{position:absolute;left:0;top:0;width:1127px;height:59px;background:var(--white);border-bottom:1px solid #d8d8d8}
.brand{position:absolute;left:62px;top:17px;font-size:21px;font-weight:300;letter-spacing:2px;color:var(--brand)}
.notify{position:absolute;top:20px;width:23px;height:21px;background:var(--brand);border-radius:2px}
.notify svg{position:absolute;left:4px;top:4px}
.badge{position:absolute;right:-7px;top:-8px;width:14px;height:14px;border-radius:50%;background:var(--crimson);color:#fff;font-size:9px;line-height:14px;text-align:center;border:1px solid #fff}
.user{position:absolute;left:955px;top:19px;display:flex;align-items:center;gap:9px;font-size:11.5px;color:#444}
.avatar{width:24px;height:24px;background:linear-gradient(135deg,#c89070,#7a4e3a)}
.sidebar{position:absolute;left:0;top:59px;width:246px;height:1141px;background:var(--side)}
.menu-toggle{position:absolute;left:214px;top:12px;width:20px;height:20px;background:var(--brand);border-radius:2px}
.menu-toggle i{position:absolute;left:4px;width:12px;height:1.5px;background:#fff}
.nav{position:absolute;left:0;top:56px;width:246px;list-style:none}
.nav li{height:35px;display:flex;align-items:center;padding-left:44px;font-size:12px;color:#fff;border-bottom:1px solid var(--side-line);position:relative}
.nav li svg{position:absolute;left:16px;top:9px}
.nav li.active{background:var(--brand);height:34px}
.nav li.active:after{content:"";position:absolute;right:0;top:11px;border:6px solid transparent;border-right-color:var(--page)}
.crumb{position:absolute;left:274px;top:77px;font-size:12px;color:#555;display:flex;align-items:center;gap:5px}
.tile{position:absolute;top:115px;width:390px;height:127px;background:#fff;border:1px solid var(--line)}
.tile-head{height:97px;position:relative;color:#fff}
.tile-head svg{position:absolute;left:19px;top:17px}
.tile-title{position:absolute;right:15px;top:27px;font-size:21px;font-weight:300;text-align:right}
.tile-sub{position:absolute;right:13px;top:55px;font-size:12px}
.tile-foot{height:29px;display:flex;align-items:center;justify-content:space-between;padding:0 10px 0 19px;font-size:11.5px;letter-spacing:.3px}
.tile.blue .tile-head{background:var(--brand)} .tile.blue .tile-foot{color:var(--brand)}
.tile.red .tile-head{background:var(--crimson)} .tile.red .tile-foot{color:var(--crimson);padding-left:14px}
.panel{position:absolute;background:#fdfdfd;border:1px solid var(--line)}
.panel-head{height:31px;display:flex;align-items:center;gap:8px;padding-left:12px;color:#fff;font-size:13.5px;margin:-1px -1px 0}
.welcome{left:274px;top:266px;width:808px;height:151px}
.welcome .panel-head{background:var(--brand)}
.status{position:absolute;left:14px;top:49px;font-size:11px;color:#222}
.ok{position:absolute;right:16px;top:45px;width:111px;height:26px;background:var(--ok);color:#fff;font-size:13px;text-align:center;line-height:26px}
.intro{position:absolute;left:14px;top:80px;right:20px;font-size:10px;line-height:16.5px;color:#555}
.trend{left:274px;top:441px;width:808px;height:277px}
.trend .panel-head{background:var(--orange)}
.trend svg.chart{position:absolute;left:0;top:30px}
.pie{top:741px;width:390px;height:278px}
.pie.one{left:274px} .pie.two{left:692px}
.pie.one .panel-head{background:var(--lime)} .pie.two .panel-head{background:var(--brand)}
.pie svg.disc{position:absolute;left:0;top:0}
.legend{position:absolute;left:325px;top:47px;list-style:none;font-size:9.5px;color:#777}
.legend li{height:15px;display:flex;align-items:center;gap:4px}
.legend i{width:13px;height:10px;border:1px solid #ccc}
.table-panel{top:1045px;width:390px;height:160px}
.table-panel.left{left:274px} .table-panel.right{left:692px}
.table-panel .panel-head{padding-left:19px;font-size:14px}
.table-panel.left .panel-head{background:var(--brand)}
.table-panel.right .panel-head{background:var(--coral)}
.search{position:absolute;left:18px;top:43px;width:345px;height:24px;border:1px solid #ddd;background:#f7f7f7;font-size:10.5px;color:#888;line-height:22px;padding-left:9px}
.search b{position:absolute;right:-1px;top:-1px;width:32px;height:24px;background:var(--ok)}
.search svg{position:absolute;left:8px;top:4px}
.grid{position:absolute;left:0;top:78px;width:100%;border-collapse:collapse;font-size:11px}
.grid th{height:33px;font-weight:400;color:var(--brand);font-size:13px;text-align:left;border-top:1px solid var(--line);border-bottom:1px solid var(--line)}
.grid td{height:34px;color:#444;border-bottom:1px solid var(--line)}
.grid td.link{color:var(--brand)}
.stars{color:#e03020;letter-spacing:-1px;font-size:12px}
</style>
</head>
<body>
<header class="topbar">
  <div class="brand">LOGO</div>
  <div class="notify" style="left:776px"><svg width="15" height="13" viewBox="0 0 15 13"><rect x="1" y="2" width="13" height="9" fill="none" stroke="#fff" stroke-width="1.3"/><path d="M1 2l6.5 5 6.5-5" fill="none" stroke="#fff" stroke-width="1.3"/></svg><span class="badge">5</span></div>
  <div class="notify" style="left:814px"><svg width="15" height="13" viewBox="0 0 15 13"><ellipse cx="7.5" cy="5.5" rx="6.5" ry="4.5" fill="#fff"/><path d="M3 9l-1 4 5-3z" fill="#fff"/></svg><span class="badge">1</span></div>
  <div class="notify" style="left:851px"><svg width="15" height="14" viewBox="0 0 15 14"><path d="M7.5 1c3 0 4 2.5 4 5v3l1.5 2H2l1.5-2V6c0-2.5 1-5 4-5z" fill="#fff"/><circle cx="7.5" cy="12.5" r="1.5" fill="#fff"/></svg><span class="badge">3</span></div>
  <div class="user"><div class="avatar" role="img" aria-label="Profilfoto des Arztes"></div><span>Dr. Lorin Vesk &#8964;</span></div>
</header>

<aside class="sidebar">
  <div class="menu-toggle"><i style="top:5px"></i><i style="top:9px"></i><i style="top:13px"></i></div>
  <ul class="nav">
    <li class="active"><svg width="18" height="16" viewBox="0 0 18 16"><path d="M9 1L1 8h2.5v7h4v-5h3v5h4V8H17z" fill="#fff"/></svg>Dasboard</li>
    <li><svg width="18" height="17" viewBox="0 0 18 17"><circle cx="7" cy="4.5" r="3.5" fill="#fff"/><path d="M1 16c0-5 3-7 6-7s4 1 4.5 2L8 16z" fill="#fff"/><path d="M10 13l2 2 4-5" fill="none" stroke="#fff" stroke-width="1.6"/></svg>Mein Konto</li>
    <li><svg width="18" height="17" viewBox="0 0 18 17"><circle cx="7" cy="4.5" r="3.5" fill="#fff"/><path d="M1 16c0-5 3-7 6-7 2 0 3 .5 4 1.5A4 4 0 0 0 10 16z" fill="#fff"/><circle cx="14" cy="13" r="3.3" fill="#fff"/><path d="M14 11v4M12 13h4" stroke="#303030" stroke-width="1.2"/></svg>Patientenbewertungen</li>
  </ul>
</aside>

<div class="crumb"><svg width="14" height="12" viewBox="0 0 14 12"><path d="M7 0L0 6h2v6h3.5V8h3v4H12V6h2z" fill="#57aad4"/></svg>DASHBOARD</div>

<section class="tile blue" style="left:274px">
  <div class="tile-head">
    <svg width="66" height="62" viewBox="0 0 66 62"><ellipse cx="33" cy="17" rx="13" ry="16" fill="#fff"/><path d="M2 62c0-14 8-20 19-23l12 6 12-6c11 3 19 9 19 23z" fill="#fff"/></svg>
    <div class="tile-title">Profil</div><div class="tile-sub">Profile bearbeiten</div>
  </div>
  <div class="tile-foot">WEITER<svg width="18" height="18" viewBox="0 0 18 18"><circle cx="9" cy="9" r="8" fill="none" stroke="#57aad4" stroke-width="1.3"/><path d="M5 9h8M10 6l3 3-3 3" fill="none" stroke="#57aad4" stroke-width="1.3"/></svg></div>
</section>
<section class="tile red" style="left:691px">
  <div class="tile-head">
    <svg width="80" height="62" viewBox="0 0 80 62"><g fill="none" stroke="#fff" stroke-width="4"><ellipse cx="22" cy="18" rx="11" ry="14"/><ellipse cx="58" cy="18" rx="11" ry="14"/></g><path d="M2 52c0-10 6-15 14-17l6 4 6-4c8 2 14 7 14 17z" fill="#fff"/><path d="M38 52c0-10 6-15 14-17l6 4 6-4c8 2 14 7 14 17z" fill="#fff"/><ellipse cx="40" cy="22" rx="12" ry="15" fill="#fff" stroke="#bf0000" stroke-width="3"/><path d="M17 62c0-13 8-19 17-21l6 5 6-5c9 2 17 8 17 21z" fill="#fff" stroke="#bf0000" stroke-width="3"/></svg>
    <div class="tile-title">Profil</div><div class="tile-sub">Profile bearbeiten</div>
  </div>
  <div class="tile-foot">ALLE ANSEHEN<svg width="18" height="18" viewBox="0 0 18 18"><circle cx="9" cy="9" r="8" fill="none" stroke="#bf0000" stroke-width="1.3"/><path d="M5 9h8M10 6l3 3-3 3" fill="none" stroke="#bf0000" stroke-width="1.3"/></svg></div>
</section>

<section class="panel welcome">
  <div class="panel-head"><svg width="18" height="14" viewBox="0 0 18 14"><rect x="1" y="3" width="16" height="10" rx="1.5" fill="#fff"/><rect x="6" y="0.8" width="6" height="3" fill="none" stroke="#fff" stroke-width="1.4"/><circle cx="9" cy="8" r="3" fill="#57aad4"/><path d="M9 6.3v3.4M7.3 8h3.4" stroke="#fff" stroke-width="1.1"/></svg>Willkommen: Dr. Halberg</div>
  <p class="status">Der Status Ihers offentlichen Profils ist derzeit:</p>
  <div class="ok">Alles OK</div>
  <p class="intro">Lorem Ipsum is simply dummy text of the printing and typesetting industry. Lorem Ipsum has been the industry's standard dummy text ever since the 1500s, when an unknown printer took a galley of type and scrambled it to make a type specimen book. It has survived not only five centuries, but also the leap into electronic typesetting, remaining essentially unchanged.</p>
</section>

<section class="panel trend">
  <div class="panel-head"><svg width="22" height="18" viewBox="0 0 22 18"><rect x="1" y="12" width="3" height="6" fill="#fff"/><rect x="6" y="9" width="3" height="9" fill="#fff"/><rect x="11" y="10" width="3" height="8" fill="#fff"/><rect x="16" y="6" width="3" height="12" fill="#fff"/><path d="M1 9l6-5 5 3 7-6" fill="none" stroke="#fff" stroke-width="1.5"/><path d="M16 1h4v4" fill="none" stroke="#fff" stroke-width="1.5"/></svg>Trendo Trend fur:</div>
  <svg class="chart" width="808" height="247" viewBox="0 0 808 247" font-family="Open Sans, sans-serif">
    <g stroke="#eee" stroke-width="1">
      <line x1="32" y1="21" x2="785" y2="21"/><line x1="32" y1="79" x2="785" y2="79"/><line x1="32" y1="138" x2="785" y2="138"/><line x1="32" y1="196" x2="785" y2="196"/><line x1="32" y1="21" x2="32" y2="196"/>
    </g>
    <g font-size="10" fill="#555" text-anchor="end">
      <text x="25" y="25">15</text><text x="25" y="83">10</text><text x="25" y="142">5</text><text x="25" y="200">0</text>
    </g>
    <path d="M368 184L410 149L452 184L493 161L535 161L577 149L619 173L660 138L702 138L743 149L785 126V196H368z" fill="#f8e3b6"/>
    <path d="M35 184H368L410 149V68L452 33L493 79L535 56L577 91L619 126L660 56L702 103L743 79L785 33" fill="none" stroke="#f95f2d" stroke-width="1.6"/>
    <g fill="#f2b632" stroke="#fff" stroke-width="1.5">
      <circle cx="452" cy="184" r="4.5"/><circle cx="493" cy="161" r="4.5"/><circle cx="535" cy="161" r="4.5"/><circle cx="577" cy="149" r="4.5"/><circle cx="619" cy="173" r="4.5"/><circle cx="660" cy="138" r="4.5"/><circle cx="702" cy="138" r="4.5"/><circle cx="743" cy="149" r="4.5"/><circle cx="785" cy="126" r="4.5"/>
    </g>
    <g fill="#f95f2d" stroke="#fff" stroke-width="1.5">
      <circle cx="368" cy="184" r="4.5"/><circle cx="410" cy="149" r="4.5"/><circle cx="410" cy="68" r="4.5"/><circle cx="452" cy="33" r="4.5"/><circle cx="493" cy="79" r="4.5"/><circle cx="535" cy="56" r="4.5"/><circle cx="577" cy="91" r="4.5"/><circle cx="619" cy="126" r="4.5"/><circle cx="660" cy="56" r="4.5"/><circle cx="702" cy="103" r="4.5"/><circle cx="743" cy="79" r="4.5"/><circle cx="785" cy="33" r="4.5"/>
    </g>
    <g font-size="11.5" fill="#555" text-anchor="middle">
      <text x="91" y="225">October 2012</text><text x="205" y="225">January 2013</text><text x="310" y="225">April 2013</text><text x="413" y="225">July 2013</text><text x="518" y="225">October 2013</text><text x="635" y="225">January 2014</text><text x="744" y="225">April 2014</text>
    </g>
  </svg>
</section>

<section class="panel pie one">
  <div class="panel-head"><svg width="16" height="16" viewBox="0 0 16 16"><path d="M8 8V1a7 7 0 1 1-6.1 3.5z" fill="#fff"/><path d="M7 7V0A7 7 0 0 0 1 3.5z" fill="#fff"/></svg>Pie 1</div>
  <svg class="disc" width="390" height="278" viewBox="0 0 390 278">
    <g stroke="#fff" stroke-width="2.5" stroke-linejoin="round">
      <path d="M190 152V46A106 106 0 0 1 206.6 256.7z" fill="#fdc914"/>
      <path d="M190 152L206.6 256.7A106 106 0 0 1 112.5 224.3z" fill="#7cc8f4"/>
      <path d="M190 152L112.5 224.3A106 106 0 0 1 190 46z" fill="#f36145"/>
    </g>
  </svg>
  <ul class="legend">
    <li><i style="background:#fdc914"></i>Series1</li><li><i style="background:#3fb0f0"></i>Series2</li><li><i style="background:#f36145"></i>Series3</li>
  </ul>
</section>

<section class="panel pie two">
  <div class="panel-head"><svg width="16" height="16" viewBox="0 0 16 16"><path d="M8 8V1a7 7 0 1 1-6.1 3.5z" fill="#fff"/><path d="M7 7V0A7 7 0 0 0 1 3.5z" fill="#fff"/></svg>Pie 2</div>
  <svg class="disc" width="390" height="278" viewBox="0 0 390 278">
    <g stroke="#fff" stroke-width="2.5" stroke-linejoin="round">
      <path d="M191 152V46A106 106 0 0 1 213 48.3z" fill="#fdc008"/>
      <path d="M191 152L213 48.3A106 106 0 0 1 273.4 85.3z" fill="#7cc8f4"/>
      <path d="M191 152L273.4 85.3A106 106 0 0 1 213 255.7z" fill="#f36145"/>
      <path d="M191 152L213 255.7A106 106 0 0 1 87.3 174z" fill="#4fc34d"/>
      <path d="M191 152L87.3 174A106 106 0 0 1 191 46z" fill="#b065fb"/>
    </g>
  </svg>
  <ul class="legend">
    <li><i style="background:#fdc008"></i>Series1</li><li><i style="background:#3fb0f0"></i>Series2</li><li><i style="background:#e8241c"></i>Series3</li><li><i style="background:#3fb83a"></i>Series4</li><li><i style="background:#a54cf5"></i>Series5</li>
  </ul>
</section>

<section class="panel table-panel left">
  <div class="panel-head">Stat 1</div>
  <div class="search">Search<b><svg width="17" height="16" viewBox="0 0 17 16"><circle cx="6" cy="6" r="4.5" fill="none" stroke="#fff" stroke-width="2"/><path d="M9.5 9.5L15 14" stroke="#fff" stroke-width="2.5"/></svg></b></div>
  <table class="grid">
    <tr><th style="padding-left:19px;width:104px">Name</th><th style="width:94px">Position</th><th style="width:110px">Start Date</th><th>Salary</th></tr>
    <tr><td style="padding-left:19px">Gerda</td><td>Chefin</td><td>1.11.2013</td><td>Salami</td></tr>
  </table>
</section>

<section class="panel table-panel right">
  <div class="panel-head">Sternchen</div>
  <div class="search">Search<b><svg width="17" height="16" viewBox="0 0 17 16"><circle cx="6" cy="6" r="4.5" fill="none" stroke="#fff" stroke-width="2"/><path d="M9.5 9.5L15 14" stroke="#fff" stroke-width="2.5"/></svg></b></div>
  <table class="grid">
    <tr><th style="padding-left:18px;width:176px">Name</th><th style="width:124px">Profileseite.</th><th>Bewertung</th></tr>
    <tr><td class="link" style="padding-left:18px">› Ciao</td><td class="link">› xyz ubgelost</td><td class="stars">★★★★★</td></tr>
  </table>
</section>
</body>
</html>
```